Trade Show Booth

We need a Single booth design size and below are the requirements from the event holder.
How to provide graphics:
Single booth: Graphic size is 1993 mm width x 2483 mm height
Naming file: Name the files as Company name_ size_scale_bleed, for example: “Roam Kestal_1993x2483mm_scale1_10_ bleed50mm.”
Bleed & Marks: 50mm bleed all around, no marks, and no crop marks.
Resolution: Please try to keep graphics over 100 dpi to maintain good quality.

We are a DMC in Iceland and will be participating in a Travel show.
www.brightfjordtrips.example

We would like to work with someone who could help us create this and potentially some marketing material for the show.

```html
<!DOCTYPE html>
<html lang="en">
<head>
<meta charset="utf-8">
<title>Roam Kestal – Booth A15 Graphic</title>
<link rel="stylesheet" href="https://fonts.googleapis.com/css2?family=League+Spartan:wght@700;800;900&family=Montserrat:wght@500;600;700;800&family=Allura&family=Oswald:wght@500;600&family=Arimo:wght@500;600&display=swap">
<style>
  :root{
    --page:#cdcdcd;
    --navy:#0d1f7a;
    --sky-top:#123349;
    --sky-mid:#1f6a5a;
    --sky-low:#2c4a5c;
    --mountain:#5d6c78;
    --cyan:#63e0f0;
    --yellow:#f5d20a;
    --blue:#3a8fe0;
    --red:#d0102a;
    --red-dark:#a80a20;
    --ink:#1a1a2e;
    --snow:#f3f5f7;
    --snow-shade:#dde2e7;
    --white:#ffffff;
  }
  *{box-sizing:border-box;margin:0;padding:0}
  html,body{width:1200px;height:2459px;overflow:hidden}
  body{background:var(--page);position:relative;font-family:"Montserrat",sans-serif}

  .booth-graphic{
    position:absolute;left:50px;top:545px;width:1100px;height:1370px;
    overflow:hidden;background:var(--snow);
    box-shadow:0 8px 22px rgba(0,0,0,.28);
  }
  .sky-scene{
    position:absolute;left:0;top:0;width:1100px;height:820px;
    background:linear-gradient(180deg,var(--sky-top) 0%,var(--sky-mid) 40%,var(--sky-low) 72%,var(--mountain) 100%);
  }
  .snowfield{position:absolute;left:0;top:560px;width:1100px;height:810px}

  .abs{position:absolute}
  .brand-name{left:0;width:1100px;top:150px;text-align:center;color:var(--white);
    font:800 50px/1 "Montserrat",sans-serif;letter-spacing:1px}
  .tagline-script{left:0;width:1100px;top:228px;text-align:center;color:var(--cyan);
    font:400 112px/1 "Allura",cursive}
  .headline-big{left:0;width:1100px;top:326px;text-align:center;
    font:900 176px/1 "League Spartan",sans-serif;letter-spacing:-2px;
    background:linear-gradient(100deg,#b9f3ff 0%,#5fe0c9 35%,#d8fff0 55%,#6fd2ff 80%,#c6f6ff 100%);
    -webkit-background-clip:text;background-clip:text;color:transparent;
    filter:drop-shadow(3px 4px 0 rgba(10,22,96,.8))}
  .headline-sub{left:0;width:1100px;top:476px;text-align:center;color:var(--yellow);
    font:800 80px/1 "League Spartan",sans-serif;text-shadow:3px 3px 0 rgba(0,0,0,.45)}
  .agency-box{left:415px;top:544px;width:295px;height:90px;background:var(--navy);
    border:2px solid #3a6ad0;color:var(--white);text-align:center;
    font:800 64px/96px "League Spartan",sans-serif}

  .explore-line{left:72px;top:784px;color:var(--ink);font:500 36px/1 "Montserrat",sans-serif}
  .explore-accent{left:72px;top:822px;color:var(--blue);font:800 41px/1 "League Spartan",sans-serif}
  .services-bar{left:72px;top:866px;width:380px;height:38px;background:var(--navy);border-radius:6px;
    color:var(--white);text-align:center;font:800 24px/38px "Montserrat",sans-serif;letter-spacing:4px}
  .services-bar span{color:var(--yellow)}

  .hiker-photo{left:0;top:920px;width:190px;height:440px;
    background:linear-gradient(180deg,var(--snow-shade) 0%,var(--snow) 100%)}

  .service-list{left:208px;top:936px;list-style:none;color:var(--ink);
    font:600 26px/29px "Arimo",sans-serif}
  .service-list li{position:relative;padding-left:25px;margin-bottom:14px}
  .service-list li::before{content:"";position:absolute;left:0;top:10px;width:11px;height:11px;
    border-radius:50%;background:var(--navy)}

  .booth-label{left:520px;width:180px;top:784px;text-align:center;color:var(--navy);
    font:800 42px/1 "League Spartan",sans-serif}
  .booth-number{left:520px;width:180px;top:822px;text-align:center;color:var(--red);
    font:800 60px/1 "League Spartan",sans-serif}

  .offer-seal{left:485px;top:895px;width:238px;height:238px}
  .offer-text{left:485px;top:895px;width:238px;height:238px;text-align:center;padding-top:62px}
  .offer-kicker{color:var(--white);font:700 13px/1 "Montserrat",sans-serif;letter-spacing:3px}
  .offer-main{color:var(--yellow);font:600 34px/1.02 "Oswald",sans-serif;margin-top:8px}

  .snapshot{background:var(--white);padding:10px;box-shadow:0 4px 12px rgba(0,0,0,.3)}
  .snapshot div{width:100%;height:100%}
  .snapshot-atv{left:705px;top:690px;width:300px;height:215px;transform:rotate(-3deg)}
  .snapshot-atv div{background:linear-gradient(180deg,#c99261 0%,#5d6673 45%,#3a3633 100%)}
  .snapshot-lagoon{left:713px;top:885px;width:300px;height:235px;transform:rotate(3deg)}
  .snapshot-lagoon div{background:linear-gradient(180deg,#7db8e6 0%,#dcebf5 55%,#8fbcd8 100%)}

  .partner-row{left:478px;top:1172px;width:560px;height:52px;display:flex;align-items:center;gap:30px}
  .partner-badge{flex:none;background:#dfe4ea;border:2px solid #7f8fa6}
  .partner-badge.square{width:42px;height:48px;border-radius:4px}
  .partner-badge.circle{width:48px;height:48px;border-radius:50%;background:#c9d6ef;border-color:var(--navy)}
  .partner-badge.wide{width:96px;height:26px;border-radius:4px;background:#e4b3b9;border-color:#e4b3b9}
  .partner-badge.dark{width:52px;height:52px;border-radius:2px;background:#111;border-color:#111}
  .partner-badge.teal{width:40px;height:40px;border-radius:50%;background:#4fb8b4;border-color:#4fb8b4}

  .web-bar{left:476px;top:1240px;width:624px;height:52px;background:var(--navy);
    border-radius:14px 0 0 14px;color:var(--white);padding-left:22px;
    font:600 26px/52px "Montserrat",sans-serif;letter-spacing:3px;white-space:nowrap}
  .web-bar span{color:#5aa6f0}
</style>
</head>
<body>
  <main class="booth-graphic">
    <div class="sky-scene" role="img" aria-label="Photo of northern lights over snowy Icelandic mountains"></div>
    <svg class="snowfield" viewBox="0 0 1100 810" aria-hidden="true">
      <defs>
        <linearGradient id="snow" x1="0" y1="0" x2="0" y2="1">
          <stop offset="0" stop-color="#e9eef2"/>
          <stop offset=".4" stop-color="#f3f5f7"/>
          <stop offset="1" stop-color="#eef1f4"/>
        </linearGradient>
      </defs>
      <path d="M0 200 C 80 170 120 150 200 160 C 300 175 360 260 470 285 C 560 300 620 240 700 215 C 790 185 850 150 930 170 C 1010 190 1060 170 1100 150 L1100 810 L0 810 Z" fill="url(#snow)"/>
    </svg>

    <div class="abs brand-name">ROAM KESTAL</div>
    <div class="abs tagline-script">Join Iceland's</div>
    <div class="abs headline-big">BIGGEST</div>
    <div class="abs headline-sub">TRAVEL &amp; TOURISM</div>
    <div class="abs agency-box">AGENCY</div>

    <div class="abs explore-line">EXPLORE THE</div>
    <div class="abs explore-accent">BEAUTY OF ICELAND</div>
    <div class="abs services-bar">SERVICES <span>WE OFFER</span></div>

    <div class="abs hiker-photo" role="img" aria-label="Photo of a hiker with backpack and trekking poles in snow"></div>

    <ul class="abs service-list">
      <li>Caves &amp;<br>Horseback Riding</li>
      <li>ATV Tour</li>
      <li>Boat Trip</li>
      <li>Sightseeing</li>
      <li>Glacier Walks</li>
      <li>Whale Watching</li>
      <li>Buggy Tour</li>
      <li>Jeep Tours</li>
    </ul>

    <div class="abs booth-label">BOOTH</div>
    <div class="abs booth-number">A15</div>

    <svg class="abs offer-seal" viewBox="0 0 200 200" aria-hidden="true">
      <polygon fill="var(--red-dark)" points="100,4 112,20 130,9 136,29 156,24 156,44 176,45 170,64 189,71 178,87 194,100 178,113 189,129 170,136 176,155 156,156 156,176 136,171 130,191 112,180 100,196 88,180 70,191 64,171 44,176 44,156 24,155 30,136 11,129 22,113 6,100 22,87 11,71 30,64 24,45 44,44 44,24 64,29 70,9 88,20"/>
      <circle cx="100" cy="100" r="78" fill="var(--red)"/>
    </svg>
    <div class="abs offer-text">
      <div class="offer-kicker">WE ALSO OFFER</div>
      <div class="offer-main">CUSTOMIZED<br>TRAVEL<br>EXPERIENCE</div>
    </div>

    <div class="abs snapshot snapshot-atv"><div role="img" aria-label="Photo of ATV riders on volcanic terrain at sunset"></div></div>
    <div class="abs snapshot snapshot-lagoon"><div role="img" aria-label="Photo of a boat among icebergs in a glacier lagoon"></div></div>

    <div class="abs partner-row">
      <span class="partner-badge square"></span>
      <span class="partner-badge circle"></span>
      <span class="partner-badge wide"></span>
      <span class="partner-badge wide"></span>
      <span class="partner-badge dark"></span>
      <span class="partner-badge teal"></span>
    </div>

    <div class="abs web-bar">www.<span>brightfjordtrips</span>.example</div>
  </main>
</body>
</html>
```